Spiritual journeyer, astrologer, Reiki master, underground music lover needs business card design

Initially I need a business card design (and possibly a logo for my new website). I offer astrological and energetic inquiry and guidance to clients in support of their life's evolutionary path. I combine an eclectic mix of methods with a focus on the mind body connection. I am a spiritual journeyer, astrologer, Reiki Master, certified personal trainer, soon to be black belt in Taekwondo (karate), and researcher into the benefits of music/sound vibrational therapy. And underground music lover :) The attached drawing is just something I drew freehand, it is symbolic of many things important to me. I wanted the figure to clearly be female. Her arms are open to catch the sky, the name of my new business is Orlabrook, and Orla is my daughter's name. This was just an idea I had, I'm open to suggestions. The photo is me with the planets in the sky as they were at the moment I was born (some years ago-LOL)
Updates

I have picked a final design. Thank you everyone for your time and effort.

Target Market(s)

Worldwide, what I do can be done in person or anywhere in the world via Skype

Industry/Entity Type

Professional Service

Contact Information for Business Card

Simple, unusual image with my business name and contact info

Font styles to use
Sans Serif

Requirements
Must have
• My website very clean, simple. Somehow combine biz name of Orlabrook with female figure catching/holding the starry sky? See my poor drawing I attached.
Nice to have
• Something that conveys all the unique, unusual, eclectic skills and capacities I have
Should not have
• Frilly, fancy, stuffy

```html
<!DOCTYPE html>
<html lang="en">
<head>
<meta charset="utf-8">
<title>Orlabrook – Business Card</title>
<link rel="stylesheet" href="https://fonts.googleapis.com/css2?family=Arimo:wght@400;600;700&family=Delius&display=swap">
<style>
  :root {
    --night: #0f0c52;
    --paper: #ffffff;
    --star: #f7e414;
    --ink: #1a1760;
    --backdrop: #ececec;
  }
  html, body {
    margin: 0;
    padding: 0;
    width: 1200px;
    height: 867px;
    overflow: hidden;
    background: var(--backdrop);
  }
  .card {
    position: absolute;
    left: 160px;
    top: 160px;
    width: 880px;
    height: 547px;
    border-radius: 30px;
    overflow: hidden;
    background: var(--paper);
  }
  .night-band {
    position: absolute;
    left: 0;
    top: 0;
    width: 100%;
    height: 300px;
    background: var(--night);
  }
  .holder-name {
    position: absolute;
    left: 72px;
    top: 130px;
    margin: 0;
    font-family: "Delius", sans-serif;
    font-size: 35px;
    font-weight: 400;
    letter-spacing: 1px;
    color: var(--star);
  }
  .holder-role {
    position: absolute;
    left: 72px;
    top: 198px;
    margin: 0;
    font-family: "Arimo", sans-serif;
    font-weight: 600;
    font-size: 23px;
    line-height: 31px;
    color: var(--paper);
  }
  .holder-role .wide { letter-spacing: 2.2px; word-spacing: 4px; }
  .contact-list {
    position: absolute;
    left: 74px;
    top: 355px;
    margin: 0;
    padding: 0;
    list-style: none;
    font-family: "Arimo", sans-serif;
    font-size: 21px;
    color: var(--ink);
  }
  .contact-list li {
    display: flex;
    align-items: center;
    height: 37px;
  }
  .contact-list svg {
    width: 20px;
    height: 20px;
    margin-right: 12px;
    flex: none;
  }
  .brand-mark {
    position: absolute;
    left: 452px;
    top: 44px;
    width: 414px;
    height: 414px;
    box-sizing: border-box;
    border-radius: 50%;
    background: var(--paper);
    border: 9px solid var(--star);
    display: flex;
    align-items: center;
    justify-content: center;
  }
  .brand-name {
    font-family: "Arimo", sans-serif;
    font-weight: 600;
    font-size: 40px;
    letter-spacing: 6px;
    color: var(--ink);
  }
</style>
</head>
<body>
  <div class="card">
    <div class="night-band"></div>

    <h1 class="holder-name">Marianne Holloway</h1>
    <p class="holder-role">Astrological and Energetic<br><span class="wide">Guidance and Inquiry</span></p>

    <ul class="contact-list">
      <li>
        <svg viewBox="0 0 20 20" aria-hidden="true"><path d="M5 2 L8 6 L6.5 8 Q8 12 12 13.5 L14 12 L18 15 L16 18 Q9 18 5 12 Q2 7 5 2 Z" fill="var(--ink)"/></svg>
        555-210-4736
      </li>
      <li>
        <svg viewBox="0 0 20 20" aria-hidden="true"><rect x="2" y="4.5" width="16" height="11" fill="none" stroke="var(--ink)" stroke-width="1.6"/><path d="M2 4.5 L10 11 L18 4.5" fill="none" stroke="var(--ink)" stroke-width="1.6"/></svg>
        Marianne.Holloway@orlabrook.com
      </li>
      <li>
        <svg viewBox="0 0 20 20" aria-hidden="true"><g fill="none" stroke="var(--ink)" stroke-width="1.4"><circle cx="10" cy="10" r="8"/><ellipse cx="10" cy="10" rx="3.5" ry="8"/><line x1="2" y1="10" x2="18" y2="10"/><line x1="10" y1="2" x2="10" y2="18"/></g></svg>
        www.orlabrook.com
      </li>
    </ul>

    <div class="brand-mark">
      <span class="brand-name">ORLABROOK</span>
    </div>
  </div>
</body>
</html>
```